Mobile Product Filter for Luxury footwear e-commerce store

We would like to see designs for a "Mobile First" product filter for our collection pages:
http://store.quellaridge.ca/collections/mukluks

The design should have a high degree of mobile usability and fit with the current look & feel.

Filtering options would be:

- Category: Mukluks / Moccasins / Talewalkers / Accessories
- Size: 5,6,7,8,9,10,11,12,13
- Gender: Male / Female / Unisex / Kids
- Color: Ideally show color swatches otherwise color names (Tan / Stone / Black / Cocoa /Tobacco / Russet)
- Sole: Grivex / Crepe / Leather
- Materials: Fur / Faux Fur / No Fur
- Production: Made in Canada / International
- Price: Up to $100 / $100 to $500 / $500 and more
- In Stock: Yes / No

** Sorting Options**
- Most Popular
- Highest Rates
- Price: High to Low
- Price: Low to High

BONUS POINTS: Provide the desktop view as well.

Target Market(s)

Women

Industry/Entity Type

E-Commerce

Number of Pages Required

2 page

Font styles to use
Sans Serif

Requirements
Must have
• Mobile first design
Nice to have
• Desktop design

```html
<!DOCTYPE html>
<html lang="en">
<head>
<meta charset="utf-8">
<title>Quellaridge – Mobile Product Filter</title>
<link href="https://fonts.googleapis.com/css2?family=PT+Sans:wght@400;700&display=swap" rel="stylesheet">
<style>
:root{
  --page-bg:#ebebef;
  --screen-bg:#ffffff;
  --header-dark:#141414;
  --header-mid:#2a2a2a;
  --accent:#e5553b;
  --accent-light:#ec6a52;
  --band:#f4f4f4;
  --card-border:#ececec;
  --text:#444444;
  --muted:#666666;
  --box-border:#c9c9c9;
  --message-bar:#3b3b3b;
  --white:#ffffff;
}
*{box-sizing:border-box;margin:0;padding:0}
html,body{width:1200px;height:2791px;overflow:hidden;background:var(--page-bg);font-family:"PT Sans",Arial,sans-serif;color:var(--text)}
.screen{position:absolute;left:298px;top:320px;width:614px;height:2195px;background:var(--screen-bg);overflow:hidden}
.app-header{position:absolute;left:0;top:0;width:614px;height:91px;background:linear-gradient(180deg,var(--header-mid),var(--header-dark));display:flex;align-items:center;justify-content:center}
.home-link{position:absolute;left:30px;top:28px;width:42px;height:36px}
.brand-name{font-size:28px;font-weight:700;color:var(--white);letter-spacing:1px}
.menu-toggle{position:absolute;right:0;top:0;width:102px;height:91px;background:var(--accent);display:flex;align-items:center;justify-content:center;gap:6px}
.menu-toggle span{display:block;width:5px;height:30px;background:var(--white)}
.filter-card{position:absolute;left:30px;width:551px;border:2px solid var(--card-border);border-radius:4px;background:var(--screen-bg)}
.card-title{position:relative;height:56px;background:var(--band);text-align:center;font-size:25px;line-height:56px;color:#3a3a3a;text-transform:uppercase}
.card-title::after{content:"";position:absolute;left:50%;bottom:-12px;margin-left:-12px;border-left:12px solid transparent;border-right:12px solid transparent;border-top:12px solid var(--band)}
.button-grid{display:grid;grid-template-columns:234px 234px;column-gap:26px;row-gap:23px;padding:32px 0 0 28px}
.pill{height:45px;background:linear-gradient(180deg,var(--accent-light),var(--accent));color:var(--white);border-radius:3px;font-size:23px;display:flex;align-items:center;justify-content:center}
.options{display:grid;padding:36px 0 0 26px;row-gap:24px;font-size:20px;color:var(--muted)}
.options.sizes{grid-template-columns:repeat(7,74px)}
.options.four{grid-template-columns:112px 126px 124px 110px}
.options.three{grid-template-columns:138px 170px 160px}
.options.colors{grid-template-columns:170px 170px 170px;padding-top:34px}
.option{display:flex;align-items:center;gap:12px;white-space:nowrap}
.box{width:19px;height:19px;border:2px solid var(--box-border);border-radius:2px;background:var(--white);flex:none;display:flex;align-items:center;justify-content:center}
.box svg{width:14px;height:14px}
.swatch{width:19px;height:19px;flex:none;margin-left:-2px}
.radio{width:22px;height:22px;border-radius:50%;border:2px solid #e2e2e2;flex:none}
.radio.selected{background:#b8231c;border-color:#b8231c;display:flex;align-items:center;justify-content:center}
.radio.selected svg{width:14px;height:14px}
.option.active{color:var(--accent)}
.price-options{grid-template-columns:180px 210px 140px}
.sort-split{height:45px;display:flex;border-radius:3px;overflow:hidden;border:2px solid var(--band)}
.sort-split .label{background:var(--accent);color:var(--white);font-size:22px;padding:0 10px;display:flex;align-items:center}
.sort-split .value{flex:1;background:var(--band);font-size:21px;color:var(--muted);display:flex;align-items:center;padding-left:14px}
.message-bar{position:absolute;left:30px;top:2146px;width:551px;height:52px;background:var(--message-bar);color:var(--white);font-size:23px;display:flex;align-items:center;justify-content:space-between;padding:0 20px;border-radius:3px 3px 0 0}
</style>
</head>
<body>
<main class="screen">
  <header class="app-header">
    <svg class="home-link" viewBox="0 0 42 36" aria-label="Home"><path d="M21 2 L2 19 H8 V34 H17 V24 H25 V34 H34 V19 H40 Z" fill="#fff"/></svg>
    <span class="brand-name">QUELLARIDGE</span>
    <div class="menu-toggle" aria-label="Menu"><span></span><span></span><span></span></div>
  </header>

  <section class="filter-card" style="top:140px;height:244px">
    <h2 class="card-title">Category</h2>
    <div class="button-grid">
      <div class="pill">Mukluks</div><div class="pill">Moccasins</div>
      <div class="pill">Talewalkers</div><div class="pill">Moccasins</div>
    </div>
  </section>

  <section class="filter-card" style="top:409px;height:141px">
    <h2 class="card-title">Size</h2>
    <div class="options sizes">
      <label class="option"><span class="box"><svg viewBox="0 0 14 14"><path d="M2 7 L6 11 L12 3" stroke="#555" stroke-width="2" fill="none"/></svg></span>5</label>
      <label class="option"><span class="box"></span>6</label>
      <label class="option"><span class="box"></span>7</label>
      <label class="option"><span class="box"></span>8</label>
      <label class="option"><span class="box"></span>9</label>
      <label class="option"><span class="box"></span>10</label>
      <label class="option"><span class="box"></span>11</label>
    </div>
  </section>

  <section class="filter-card" style="top:580px;height:141px">
    <h2 class="card-title">Gender</h2>
    <div class="options four">
      <label class="option"><span class="box"><svg viewBox="0 0 14 14"><path d="M2 7 L6 11 L12 3" stroke="#555" stroke-width="2" fill="none"/></svg></span>Male</label>
      <label class="option"><span class="box"></span>Female</label>
      <label class="option"><span class="box"></span>Unisex</label>
      <label class="option"><span class="box"></span>Kids</label>
    </div>
  </section>

  <section class="filter-card" style="top:753px;height:192px">
    <h2 class="card-title">Color</h2>
    <div class="options colors">
      <label class="option"><span class="box"><svg viewBox="0 0 14 14"><path d="M2 7 L6 11 L12 3" stroke="#555" stroke-width="2" fill="none"/></svg></span><span class="swatch" style="background:#c9a46a"></span>Tan</label>
      <label class="option"><span class="box"></span><span class="swatch" style="background:#a3a3a3"></span>Stone</label>
      <label class="option"><span class="box"></span><span class="swatch" style="background:#111"></span>Black</label>
      <label class="option"><span class="box"></span><span class="swatch" style="background:#6f5646"></span>Cocoa</label>
      <label class="option"><span class="box"></span><span class="swatch" style="background:#a9826a"></span>Tobacco</label>
      <label class="option"><span class="box"></span><span class="swatch" style="background:#a51d12"></span>Russet</label>
    </div>
  </section>

  <section class="filter-card" style="top:977px;height:141px">
    <h2 class="card-title">Sole</h2>
    <div class="options three">
      <label class="option"><span class="box"><svg viewBox="0 0 14 14"><path d="M2 7 L6 11 L12 3" stroke="#555" stroke-width="2" fill="none"/></svg></span>Grivex</label>
      <label class="option"><span class="box"></span>Crepe</label>
      <label class="option"><span class="box"></span>Leather</label>
    </div>
  </section>

  <section class="filter-card" style="top:1149px;height:141px">
    <h2 class="card-title">Materials</h2>
    <div class="options three">
      <label class="option"><span class="box"><svg viewBox="0 0 14 14"><path d="M2 7 L6 11 L12 3" stroke="#555" stroke-width="2" fill="none"/></svg></span>Fur</label>
      <label class="option"><span class="box"></span>Faux Fur</label>
      <label class="option"><span class="box"></span>No Fur</label>
    </div>
  </section>

  <section class="filter-card" style="top:1321px;height:179px">
    <h2 class="card-title">Production</h2>
    <div class="button-grid">
      <div class="pill">Made in Canada</div><div class="pill">International</div>
    </div>
  </section>

  <section class="filter-card" style="top:1525px;height:141px">
    <h2 class="card-title">Price</h2>
    <div class="options price-options">
      <label class="option active"><span class="radio selected"><svg viewBox="0 0 14 14"><path d="M2 7 L6 11 L12 3" stroke="#fff" stroke-width="2.4" fill="none"/></svg></span>Up to $100</label>
      <label class="option" style="color:#333"><span class="radio"></span>$100 to $500</label>
      <label class="option" style="color:#333"><span class="radio"></span>$500</label>
    </div>
  </section>

  <section class="filter-card" style="top:1698px;height:144px">
    <h2 class="card-title">In Stock</h2>
    <div class="options three">
      <label class="option"><span class="box"><svg viewBox="0 0 14 14"><path d="M2 7 L6 11 L12 3" stroke="#555" stroke-width="2" fill="none"/></svg></span>Yes</label>
      <label class="option"><span class="box"></span>No</label>
    </div>
  </section>

  <section class="filter-card" style="top:1871px;height:240px">
    <h2 class="card-title">Sorting Options</h2>
    <div class="button-grid" style="row-gap:23px">
      <div class="pill">Most Popular</div><div class="pill">Highest Rates</div>
      <div class="sort-split"><span class="label">Price:</span><span class="value">High to Low</span></div>
      <div class="sort-split"><span class="label">Price:</span><span class="value">Low to High</span></div>
    </div>
  </section>

  <div class="message-bar">
    <span>Leave a Message</span>
    <svg width="20" height="14" viewBox="0 0 20 14"><path d="M3 11 L10 4 L17 11" stroke="#fff" stroke-width="3" fill="none"/></svg>
  </div>
</main>
</body>
</html>
```